Business Card Design Project

Colette Marivaux logo on front of card with 'of Sydney' added in small font.
Back of card needs to include the following information :

"Pure pleasure for the discerning gentleman" (I may omit once I've seen the design)

colettemarivaux.com.au

Contact by SMS or email only :

colette@colettemarivaux.com.au
Mobile : 0483 956 204 or + 61 483 956 204

Target Market(s)

Male professionals aged 20-60.

Industry/Entity Type

Business

Requirements
Must have
• Simple, bold, stylish and elegant.

```html
<!DOCTYPE html>
<html lang="en">
<head>
<meta charset="utf-8">
<title>Colette Marivaux — Business Cards</title>
<link rel="stylesheet" href="https://fonts.googleapis.com/css2?family=Pinyon+Script&family=Questrial&display=swap">
<style>
  :root {
    --page: #ffffff;
    --card-black: #000000;
    --teal: #0a91ab;
    --gold: #a99c62;
    --ink-light: #ffffff;
  }
  html, body {
    margin: 0;
    padding: 0;
    width: 1200px;
    height: 848px;
    overflow: hidden;
    background: var(--page);
  }
  .sheet {
    position: relative;
    width: 1200px;
    height: 848px;
  }
  .card {
    position: absolute;
    width: 368px;
    height: 246px;
    box-sizing: border-box;
    color: var(--ink-light);
    font-family: "Questrial", sans-serif;
  }
  .card--front { background: var(--card-black); left: 223px; }
  .card--back { left: 603px; }
  .row-1 { top: 52px; }
  .row-2 { top: 313px; }
  .card--teal { background: var(--teal); }
  .card--gold { background: var(--gold); }

  .lockup {
    position: absolute;
    left: 0;
    right: 0;
    top: 104px;
    display: flex;
    flex-direction: column;
    align-items: center;
    gap: 9px;
  }
  .wordmark {
    display: flex;
    align-items: center;
    gap: 9px;
  }
  .wordmark__dot {
    width: 9px;
    height: 9px;
    border-radius: 50%;
  }
  .wordmark__name {
    font-size: 19px;
    line-height: 22px;
    letter-spacing: 2.5px;
    text-transform: uppercase;
    color: var(--ink-light);
    white-space: nowrap;
  }
  .locale {
    margin: 0;
    font-size: 11px;
    line-height: 12px;
    letter-spacing: 3px;
    text-transform: uppercase;
  }
  .lockup--teal .wordmark__dot { background: var(--teal); }
  .lockup--teal .locale { color: var(--teal); }
  .lockup--gold .wordmark__dot { background: var(--gold); }
  .lockup--gold .locale { color: var(--gold); }

  .tagline {
    position: absolute;
    left: 33px;
    top: 30px;
    margin: 0;
    font-family: "Pinyon Script", cursive;
    font-weight: 400;
    font-size: 29px;
    line-height: 25px;
  }
  .contact {
    position: absolute;
    top: 148px;
    font-size: 11.7px;
    line-height: 14px;
    margin: 0;
    white-space: nowrap;
  }
  .contact--web { left: 33px; }
  .contact--details { left: 175px; }
</style>
</head>
<body>
<main class="sheet">
  <section class="card card--front row-1">
    <div class="lockup lockup--teal">
      <div class="wordmark">
        <span class="wordmark__dot"></span>
        <span class="wordmark__name">Colette Marivaux</span>
      </div>
      <p class="locale">of Sydney</p>
    </div>
  </section>
  <section class="card card--back card--teal row-1">
    <h2 class="tagline">Pure pleasure for the<br>discerning gentleman.</h2>
    <p class="contact contact--web">colettemarivaux.com.au</p>
    <p class="contact contact--details">Contact by SMS or email<br>only please:<br>colette@colettemarivaux.com.au<br>0483 956 204 /<br>+ 61 483 956 204</p>
  </section>

  <section class="card card--front row-2">
    <div class="lockup lockup--gold">
      <div class="wordmark">
        <span class="wordmark__dot"></span>
        <span class="wordmark__name">Colette Marivaux</span>
      </div>
      <p class="locale">of Sydney</p>
    </div>
  </section>
  <section class="card card--back card--gold row-2">
    <h2 class="tagline">Pure pleasure for the<br>discerning gentleman.</h2>
    <p class="contact contact--web">colettemarivaux.com.au</p>
    <p class="contact contact--details">Contact by SMS or email<br>only please:<br>colette@colettemarivaux.com.au<br>0483 956 204 /<br>+ 61 483 956 204</p>
  </section>
</main>
</body>
</html>
```